Foot and ankle surgeon requires a website design

I need a website where prospective and established patients can obtain information and then direct them to making appointments. My practice is a highly professional surgical practice specialising in surgery to the foot and ankle. My title is Mr Colin Dravers, Podiatric Foot & Ankle Surgeon. My qualifications are: BSc MSc FACPS
The practice website will require information on: Locations, phone numbers to make appointments, general background on podiatric surgery,
I would like to include information on: my hospital appointments, surgical fellowships held, training programs undertaken, association memberships, publications written, links to useful websites
A page dedicated to common foot conditions would be useful and also a page with referral information including an online registration section that will be sent direct to the receptionist.
Examples of similar websites include:
http://www.jorbellianfeet.com.au/
http://www.quandrilfootsurgeon.com.au/
I will provide files on logo, self photos and my personal training history etc.
Also if there is going to be a background theme I personally am associated with surfing and beach activities, it would be great if this was able to be reflected in the design.
Thank you.

```html
<!DOCTYPE html>
<html lang="en">
<head>
<meta charset="utf-8">
<title>Mr Colin Dravers – Podiatric Foot &amp; Ankle Surgeon</title>
<link href="https://fonts.googleapis.com/css2?family=Lato:wght@300;400;700&family=Arimo:wght@400;700&display=swap" rel="stylesheet">
<style>
:root{
  --teal:#3c7d8e;
  --teal-dark:#2f6878;
  --page:#ebebeb;
  --white:#ffffff;
  --orange:#f26b1d;
  --blue:#2a6aa0;
  --navy:#1d4f7f;
  --ink:#3a3a3a;
  --muted:#777;
  --line:#d4d4d4;
  --photo-skin:#d9a98a;
  --photo-scrub:#3a8f98;
}
*{margin:0;padding:0;box-sizing:border-box}
html,body{width:800px;height:1200px;overflow:hidden}
body{position:relative;background:var(--page);font-family:'Lato',sans-serif;color:var(--ink)}
.abs{position:absolute}
.topnav{left:0;top:0;width:800px;height:38px;background:linear-gradient(var(--teal),var(--teal-dark))}
.topnav a{position:absolute;top:13px;font-size:12px;line-height:14px;color:var(--white);text-decoration:none;white-space:nowrap}
.topnav .home{left:120px;top:4px;width:62px;height:34px;background:#f4f4f4;color:#333;text-align:center;line-height:34px}
.topnav .sep{position:absolute;top:13px;width:1px;height:14px;background:#cfe3e8}
.brand{left:97px;top:56px}
.brand .mark{position:absolute;left:0;top:6px;width:22px;height:22px;border-radius:50%;background:var(--navy)}
.brand .name{position:absolute;left:24px;top:28px;white-space:nowrap;font-size:10px;color:var(--navy)}
.brand .quals{position:absolute;left:24px;top:42px;white-space:nowrap;font-size:6px;color:var(--navy)}
.brand .role{position:absolute;left:24px;top:50px;white-space:nowrap;font-size:6.5px;color:var(--orange)}
.phone-ring{left:443px;top:68px;width:36px;height:36px;border-radius:50%;background:var(--white);border:1px solid var(--line)}
.phone-num{left:487px;top:78px;font-size:15px;color:var(--navy);letter-spacing:1px;white-space:nowrap}
.search{left:612px;top:79px;width:100px;height:15px;border-radius:8px;background:var(--white);border:1px solid var(--line);font-size:7px;color:#aaa;padding:2px 6px}
.slider{left:88px;top:134px;width:624px;height:266px;background:var(--white);border:1px solid var(--line);border-radius:3px}
.slider h1{position:absolute;left:20px;top:26px;font-size:20px;font-weight:400;color:#222}
.slider p{position:absolute;left:20px;top:57px;width:262px;font-size:8.5px;line-height:16px;color:#555}
.btn{position:absolute;background:var(--orange);color:var(--white);text-align:center;border:1px solid #fbb}
.slider .btn{left:94px;top:157px;width:79px;height:27px;line-height:25px;font-size:12px}
.slider .photo{position:absolute;left:311px;top:14px;width:298px;height:197px;background:linear-gradient(120deg,var(--photo-scrub) 0 55%,var(--photo-skin) 75%,#f5f0ec)}
.slider .rule{position:absolute;left:19px;top:228px;width:585px;height:1px;background:var(--line)}
.dots{position:absolute;left:272px;top:242px;display:flex;gap:4px}
.dots span{width:8px;height:8px;border-radius:50%;border:1px solid #bbb;background:#f2f2f2}
.dots span.on{background:#555}
.steps{left:89px;top:415px}
.step-label{position:absolute;font-family:'Arimo',sans-serif;white-space:nowrap}
.step-label b{display:block;font-size:11.5px}
.step-label i{display:block;font-style:normal;font-size:7.5px;color:var(--orange);margin-top:1px}
.step-num{position:absolute;font-family:'Arimo',sans-serif;font-size:30px;font-weight:700;top:6px}
.card{top:497px;width:173px}
.card .photo{width:173px;height:111px;border:4px solid #d8d8d8;outline:1px solid #bbb}
.card h3{margin:8px 0 0 3px;font-size:14px;font-weight:400;color:var(--blue)}
.card p{margin:4px 0 0 3px;font-size:9px;line-height:11.5px;color:#444}
.welcome h2{font-size:30px;font-weight:400;color:var(--orange)}
.welcome p{width:310px;font-size:11px;line-height:20px;margin-top:4px}
.box{left:526px;width:186px;background:linear-gradient(#eeeeee,#e2e2e2);border:1px solid #d0d0d0}
.box h4{position:absolute;font-size:14px;font-weight:400;color:var(--orange);white-space:nowrap}
.box h4.appt-title{font-size:13px}
.box .news{position:absolute;left:14px;top:44px;width:150px;font-size:9px;line-height:12px}
.box .news a{color:var(--navy);font-weight:700;text-decoration:none}
.appt{position:absolute;left:20px;font-size:6.5px;color:#444;line-height:9.5px;white-space:nowrap}
.appt .d{display:inline-block;width:20px;text-align:right;padding-right:4px;border-right:2px solid var(--navy);vertical-align:top}
.appt .t{display:inline-block;padding-left:4px}
.band{left:0;top:940px;width:800px;height:157px;background:var(--white)}
.band h5{position:absolute;font-size:19px;font-weight:400;color:var(--orange);text-align:center}
.band ul{position:absolute;list-style:none;font-size:11px;line-height:15.2px;color:#333}
.band li:before{content:"• "}
.field{position:absolute;left:568px;width:144px;background:#eeeeee;font-size:7px;font-style:italic;color:#888;padding:3px 8px}
.footer{left:0;top:1097px;width:800px;height:103px;background:#e4e4e4}
.footer a{position:absolute;top:27px;font-size:9px;color:#333;text-decoration:none}
.footer .sep{position:absolute;top:24px;width:1px;height:15px;background:#666}
.footer .copy{position:absolute;left:88px;top:62px;font-size:7px;color:#555}
.footer .addr{position:absolute;right:88px;top:19px;text-align:right;font-size:8.5px;line-height:17px;color:#333}
.social{position:absolute;top:80px;width:11px;height:11px;border-radius:50%;background:var(--navy)}
</style>
</head>
<body>

<nav class="topnav abs">
  <a class="home" href="#">Home</a>
  <a href="#" style="left:198px">Appointment</a><span class="sep" style="left:285px"></span>
  <a href="#" style="left:306px">About</a><span class="sep" style="left:354px"></span>
  <a href="#" style="left:371px">Services</a><span class="sep" style="left:430px"></span>
  <a href="#" style="left:446px">Get In Touch</a>
</nav>

<div class="brand abs">
  <span class="mark"></span>
  <span class="name">Mr Colin Dravers</span>
  <span class="quals">M.Sc. B.Sc. F.A.C.P.S.</span>
  <span class="role">Podiatric Foot &amp; Ankle Surgeon</span>
</div>

<div class="phone-ring abs">
  <svg width="36" height="36" viewBox="0 0 36 36"><path d="M13 9c-2 1-3 3-2 6 2 6 6 10 11 12 3 1 5 0 6-2l-3-3-3 2c-3-1-6-5-7-8l2-3z" fill="var(--orange)"/></svg>
</div>
<div class="phone-num abs">08 9170 2284</div>
<div class="search abs">Search
  <svg class="abs" style="right:5px;top:2px" width="10" height="10" viewBox="0 0 10 10"><circle cx="4" cy="4" r="3" fill="none" stroke="#777" stroke-width="1.4"/><path d="M6 6l3 3" stroke="#777" stroke-width="1.6"/></svg>
</div>

<section class="slider abs">
  <h1>ABOUT FOOT SURGERY</h1>
  <p>Etiam dignissim lectus id diam varius egestas. Curabitur vel libero massa. Phasellus scelerisque est ac enim interdum pharetra. Nam tristique venenatis tortor non interdum. Aliquam molestie sem eget ipsum dapibus congue. Cras venenatis nisi nec est faucibus consequat.</p>
  <span class="btn">View Details</span>
  <div class="photo" role="img" aria-label="Surgeon in teal scrubs examining a patient's foot"></div>
  <div class="rule"></div>
  <div class="dots"><span class="on"></span><span></span><span></span><span></span><span></span><span></span><span></span></div>
</section>

<div class="steps abs">
  <svg class="abs" width="620" height="46" viewBox="0 0 620 46">
    <defs><linearGradient id="stepBg" x1="0" y1="0" x2="0" y2="1"><stop offset="0" stop-color="#fafafa"/><stop offset="1" stop-color="#e6e6e6"/></linearGradient>
    <linearGradient id="stepOn" x1="0" y1="0" x2="0" y2="1"><stop offset="0" stop-color="#2369a3"/><stop offset="1" stop-color="#164a7a"/></linearGradient></defs>
    <rect x="0" y="0" width="619" height="45" fill="url(#stepBg)" stroke="#ccc"/>
    <path d="M380 0l14 22.5L380 45" fill="none" stroke="#ddd" stroke-width="2"/>
    <path d="M536 0l14 22.5L536 45" fill="none" stroke="#ddd" stroke-width="2" opacity="0"/>
    <path d="M0 0h188l13 22.5L188 45H0z" fill="url(#stepOn)"/>
  </svg>
  <span class="step-num" style="left:10px;color:#fff">1</span>
  <div class="step-label" style="left:36px;top:15px;color:#fff"><b>STEP ONE</b><i>Sign Up</i></div>
  <span class="step-num" style="left:174px;color:#888">2</span>
  <div class="step-label" style="left:198px;top:15px;color:#666"><b>STEP TWO</b><i>Make an appointment</i></div>
  <span class="step-num" style="left:328px;color:#888">3</span>
  <div class="step-label" style="left:353px;top:15px;color:#666"><b>STEP THREE</b><i>Pellentesque accumsan</i></div>
  <span class="step-num" style="left:482px;color:#888">4</span>
  <div class="step-label" style="left:507px;top:15px;color:#666"><b>DONE!</b><i>Lorem ipsum dolor</i></div>
</div>

<article class="card abs" style="left:114px">
  <div class="photo" role="img" aria-label="Gloved hands examining a patient's ankle" style="background:linear-gradient(110deg,#222 0 20%,#e8e6e0 40%,#6a94c8 60%,#c9a26a)"></div>
  <h3>Lorem ipsum</h3>
  <p>Lorem ipsum is a dummy text only. Dolor sit amet, consectetur adipiscing elit. Nullam felis mauris, eleifend ac rhoncus non.</p>
</article>
<article class="card abs" style="left:314px">
  <div class="photo" role="img" aria-label="Doctor in scrubs testing a patient's foot reflex" style="background:linear-gradient(110deg,#2f8c90 0 45%,var(--photo-skin) 70%,#f6f3ef)"></div>
  <h3>Lorem ipsum</h3>
  <p>Lorem ipsum is a dummy text only. Dolor sit amet, consectetur adipiscing elit. Nullam felis mauris, eleifend ac rhoncus non.</p>
</article>
<article class="card abs" style="left:514px">
  <div class="photo" role="img" aria-label="Podiatrist examining the sole of a bare foot" style="background:linear-gradient(110deg,#4a4a4a 0 15%,#e0d8d2 40%,#d8b69c 65%,#eef0f4)"></div>
  <h3>Lorem ipsum</h3>
  <p>Lorem ipsum is a dummy text only. Dolor sit amet, consectetur adipiscing elit. Nullam felis mauris, eleifend ac rhoncus non.</p>
</article>

<section class="welcome abs" style="left:90px;top:713px">
  <h2>Welcome...</h2>
  <p>Lorem ipsum is a dummy text only. Dolor sit amet, consectetur adipiscing elit. Nullam felis mauris, eleifend ac rhoncus non, lobortis at diam. Pellentesque suscipit nulla sit amet venenatis porttitor. In augue felis.</p>
  <p>Vestibulum bibendum, nulla quis viverra pharetra, lorem dolor tincidunt turpis, ut fermentum velit ligula pretium mi. Pellentesque euismod rutrum massa.</p>
</section>

<aside class="box abs" style="top:715px;height:94px">
  <svg class="abs" style="left:14px;top:5px" width="28" height="28" viewBox="0 0 28 28"><rect x="2" y="5" width="20" height="20" fill="none" stroke="var(--orange)" stroke-width="2"/><path d="M10 18l2-5 11-11 3 3-11 11z" fill="var(--orange)"/></svg>
  <h4 style="left:49px;top:11px">Recent News</h4>
  <p class="news">Praesent venenatis nec ligula in tincidunt. Suspendisse fringilla odio non. <a href="#">Read more... &gt;&gt;</a></p>
</aside>

<aside class="box abs" style="top:817px;height:94px">
  <svg class="abs" style="left:14px;top:7px" width="24" height="24" viewBox="0 0 24 24"><rect x="1" y="3" width="22" height="20" rx="2" fill="none" stroke="var(--orange)" stroke-width="2"/><rect x="1" y="3" width="22" height="5" fill="var(--orange)"/><path d="M6 0v6M18 0v6M1 13h22M1 18h22M8 8v15M16 8v15" stroke="var(--orange)" stroke-width="1.2"/></svg>
  <h4 class="appt-title" style="left:44px;top:13px">Hospital Appointments</h4>
  <div class="appt" style="top:43px"><span class="d">July<br>16</span><span class="t">Pellentesque accumsan dignissim<br>Wed &nbsp;/ &nbsp; 9:00 am</span></div>
  <div class="appt" style="top:72px"><span class="d">July<br>18</span><span class="t">Pellentesque accumsan dignissim<br>Fri &nbsp; &nbsp;/ &nbsp; 10:00 am</span></div>
</aside>

<section class="band abs">
  <h5 style="left:76px;top:14px;width:200px">Foot Conditions</h5>
  <ul style="left:88px;top:52px"><li>Vestibulum</li><li>Eget</li><li>Fringilla</li><li>Odio</li><li>Sed commodo</li><li>Magna pretium</li></ul>
  <ul style="left:205px;top:52px"><li>Vestibulum</li><li>Eget</li><li>Fringilla</li><li>Odio</li><li>Sed commodo</li><li>Magna pretium</li></ul>

  <h5 style="left:331px;top:14px;width:160px">Gallery</h5>
  <div class="abs" role="img" aria-label="Doctor holding a patient's foot during a check-up" style="left:362px;top:42px;width:106px;height:70px;border:1px solid #ccc;background:linear-gradient(120deg,#f4f4f4 20%,#c9d3dc 45%,var(--photo-skin) 75%,#f2ece6)"></div>
  <svg class="abs" style="left:362px;top:112px" width="106" height="10" viewBox="0 0 106 10"><path d="M14 9l4-5 4 5z" fill="var(--navy)"/></svg>
  <div class="abs" role="img" aria-label="Gallery thumbnail: foot examination" style="left:365px;top:121px;width:32px;height:22px;border:2px solid var(--navy);background:linear-gradient(120deg,#eee,#d9a98a)"></div>
  <div class="abs" role="img" aria-label="Gallery thumbnail: hands on a patient's foot" style="left:401px;top:121px;width:31px;height:22px;background:linear-gradient(120deg,#e8ddd2,#c99878)"></div>
  <div class="abs" role="img" aria-label="Gallery thumbnail: foot x-ray in blue tones" style="left:436px;top:121px;width:31px;height:22px;background:linear-gradient(120deg,#2f7cc0,#bfe0f2)"></div>

  <h5 style="left:557px;top:14px;width:160px">Contact Us</h5>
  <div class="field" style="top:42px;height:15px">Enter name</div>
  <div class="field" style="top:62px;height:15px">Enter email address</div>
  <div class="field" style="top:81px;height:49px;padding-top:9px">Your message</div>
  <span class="btn" style="left:569px;top:134px;width:60px;height:16px;line-height:15px;font-size:8px;border:none">Submit</span>
</section>

<footer class="footer abs">
  <a href="#" style="left:87px">Home</a><span class="sep" style="left:130px"></span>
  <a href="#" style="left:150px">Appointment</a><span class="sep" style="left:232px"></span>
  <a href="#" style="left:258px">About</a><span class="sep" style="left:306px"></span>
  <a href="#" style="left:323px">Services</a><span class="sep" style="left:379px"></span>
  <a href="#" style="left:398px">Get In Touch</a>
  <p class="copy">Copyright © 2014. YourCompanyName. All Rights Reserved</p>
  <span class="social" style="left:88px"></span><span class="social" style="left:104px"></span><span class="social" style="left:119px"></span>
  <p class="addr">Harbourside 42 Coral Reef Parade PO Box<br>3187, Seabright WA 6012<br>P 08 9170 2284 F 08 9170 2291<br>Eastvale 7/14 Shorebreak Lane PO Box 20861,</p>
</footer>

</body>
</html>
```